"Brightwall Sound Living Residences" need a busines Card Design got Builder

We need a business card design for a company based in Milford, Michigancalled Brightwall Sound Living Residences - has been recognized as a premier custom home builder. Distinguished by outstanding craftmanship and timeless beauty. Our custom home can be found in the most prestigious communities in Michigan. The homes are built with ICF (insulated concrete homes) which is green, allergy free, fire free, mold free and quitter. Our slogan "Crafting every wall with care" and also we are ICF distributor for the state of Michigan

Target Market(s)

Anyone who is making over $100,000 a year and who wants to have totally custom built home. Ages from 29 up to 60 years old

Industry/Entity Type

Concrete

Contact Information for Business Card

we want to use - green, black, gray or blue colors - we want to look different with our business cards, because we built homes only with ICF, green, healthier and highly energy efficient homes.

Requirements
Must have
• I have logo that I attached and we have been using the logo (the only green home)
Nice to have
• should look quality business card,

Files

```html
<!DOCTYPE html>
<html lang="en">
<head>
<meta charset="utf-8">
<title>Brightwall Sound Living Residences — Business Card</title>
<link href="https://fonts.googleapis.com/css2?family=Lato:wght@400;700&family=Raleway:wght@300;400&display=swap" rel="stylesheet">
<style>
  :root {
    --backdrop: #dde3ec;
    --card-white: #fbfbfb;
    --card-black: #141414;
    --ink-dark: #2a2a2a;
    --ink-gray: #8a8a8a;
    --rule-gray: #b9b9b9;
    --brand-blue: #1f6fc8;
    --brand-indigo: #2e2a8c;
    --badge-gray: #9a9a9a;
    --white: #ffffff;
  }
  * { margin: 0; padding: 0; box-sizing: border-box; }
  html, body { width: 1200px; height: 900px; overflow: hidden; }
  body {
    background: var(--backdrop);
    font-family: "Lato", sans-serif;
    position: relative;
  }
  .card {
    position: absolute;
    left: 337px;
    width: 525px;
    height: 300px;
    overflow: hidden;
    box-shadow: 0 6px 18px rgba(40, 55, 80, 0.18);
  }
  .card--front { top: 120px; background: var(--card-white); }
  .card--back  { top: 480px; background: var(--card-black); }

  .card__art { position: absolute; inset: 0; width: 100%; height: 100%; }

  /* front */
  .brand {
    position: absolute;
    left: 190px;
    top: 52px;
    display: flex;
    align-items: center;
    gap: 12px;
  }
  .brand__dot {
    width: 40px; height: 40px;
    border-radius: 50%;
    background: var(--brand-indigo);
    flex: none;
  }
  .brand__name {
    font-family: "Raleway", sans-serif;
    font-weight: 400;
    font-size: 15px;
    line-height: 1.2;
    letter-spacing: 1px;
    text-transform: uppercase;
    color: var(--ink-gray);
  }
  .badge {
    position: absolute;
    right: 30px;
    top: 142px;
    width: 44px;
    height: 34px;
    border: 2px solid var(--badge-gray);
    background: #e4e4e4;
  }
  .person {
    position: absolute;
    left: 34px;
    top: 160px;
  }
  .person__name {
    font-weight: 700;
    font-size: 16px;
    color: var(--ink-dark);
  }
  .person__role {
    font-size: 9px;
    letter-spacing: 1px;
    color: var(--ink-gray);
    margin-top: 2px;
  }
  .contact {
    list-style: none;
    margin-top: 10px;
    font-size: 10.5px;
    color: var(--ink-gray);
  }
  .contact li { display: flex; align-items: center; gap: 7px; margin-bottom: 3px; }
  .contact svg { width: 10px; height: 10px; fill: var(--brand-blue); flex: none; }
  .web {
    position: absolute;
    right: 22px;
    bottom: 12px;
    font-size: 11px;
    color: var(--white);
    letter-spacing: 0.3px;
  }

  /* back */
  .back-mark {
    position: absolute;
    inset: 0;
    display: flex;
    align-items: center;
    justify-content: center;
    gap: 16px;
  }
  .back-mark__dot {
    width: 52px; height: 52px;
    border-radius: 50%;
    background: var(--brand-indigo);
    flex: none;
  }
  .back-mark__text { display: flex; flex-direction: column; gap: 6px; }
  .back-mark__name {
    font-family: "Raleway", sans-serif;
    font-weight: 400;
    font-size: 11px;
    letter-spacing: 1.5px;
    text-transform: uppercase;
    color: #7c8fb8;
  }
  .slogan {
    font-family: "Raleway", sans-serif;
    font-weight: 300;
    font-size: 17px;
    letter-spacing: 0.5px;
    text-transform: uppercase;
    color: var(--white);
  }
</style>
</head>
<body>

  <section class="card card--front" aria-label="Business card front">
    <svg class="card__art" viewBox="0 0 525 300" aria-hidden="true">
      <line x1="190" y1="184" x2="505" y2="184" stroke="var(--rule-gray)" stroke-width="1"/>
      <path d="M0 300 C 150 275, 300 240, 525 226 L 525 234 C 320 250, 170 282, 30 300 Z" fill="var(--brand-blue)"/>
      <path d="M200 300 C 320 262, 420 240, 525 232 L 525 300 Z" fill="var(--card-black)"/>
    </svg>

    <div class="brand">
      <span class="brand__dot"></span>
      <p class="brand__name">Brightwall Sound<br>Living Residences</p>
    </div>

    <div class="badge" aria-hidden="true"></div>

    <div class="person">
      <p class="person__name">Daniel Harlow</p>
      <p class="person__role">DIRECTOR</p>
      <ul class="contact">
        <li>
          <svg viewBox="0 0 10 10"><path d="M2 0.5 L4 2.5 L3 3.8 C3.6 5 5 6.4 6.2 7 L7.5 6 L9.5 8 L8.3 9.5 C4.5 9 1 5.5 0.5 1.7 Z"/></svg>
          555 01 482
        </li>
        <li>
          <svg viewBox="0 0 10 10"><path d="M2.5 0 H7.5 V10 H2.5 Z M3.3 1 V8 H6.7 V1 Z" fill-rule="evenodd"/></svg>
          555 01 493
        </li>
        <li>
          <svg viewBox="0 0 10 10"><path d="M0 2 H10 V8.5 H0 Z M0.8 2.6 L5 5.6 L9.2 2.6 Z" fill-rule="evenodd"/></svg>
          dharlow@brightwall-living.com
        </li>
      </ul>
    </div>

    <p class="web">www.brightwall-living.com</p>
  </section>

  <section class="card card--back" aria-label="Business card back">
    <div class="back-mark">
      <span class="back-mark__dot"></span>
      <div class="back-mark__text">
        <p class="back-mark__name">Brightwall Sound Living Residences</p>
        <p class="slogan">Crafting every wall with care</p>
      </div>
    </div>
  </section>

</body>
</html>
```